Harrowgate Distillery Bottle Label Design

We need a label design for a product called "Cedar Lorne Straight Bourbon Whiskey". The bottle has two embossments on the side and an image printed on the back that will show through when looking from the front (shown in the attached image). It's made of 30% rye and 70% corn; images of the ingredients can be incorporated into the label design. We are a distillery that produces whiskey and bourbon from local farmers around the area. We focus on the quality of the ingredients and using the recipes passed down from generation to generation. We like a straight forward design using two colors maximum. The background will be brown once filled with the bourbon, so it must contrast against it (i.e. white and other lighter colors). The Harrowgate Distillery logo must be present on the bottle front, as well as 750 ml, 84 PROOF, 42% ALC/VOL.

Target Market(s)

Craft whiskey consumers.

Industry/Entity Type

Product

Colors
fee18a
fbe7d2
fff3d1
fefcee
fefdec
fdf9cf

Requirements
Must have
• 750 ml, 84 PROOF, 42% ALC/VOL. Aged for 3 years.The Harrowgate Distillery logo must be present on the bottle. Only two colors on label.
Nice to have
• Story of how we are a micro distillery making hand crafted whiskey.
Should not have
• False or misleading print.

```html
<!DOCTYPE html>
<html lang="en">
<head>
<meta charset="utf-8">
<title>Harrowgate Distillery – Cedar Lorne Straight Bourbon Whiskey Label</title>
<link rel="stylesheet" href="https://fonts.googleapis.com/css2?family=Staatliches&family=Old+Standard+TT&display=swap">
<style>
  :root {
    --label-ground: #231f1e;
    --label-cream: #e3cfa5;
  }
  html, body {
    margin: 0;
    padding: 0;
    overflow: hidden;
    background: var(--label-ground);
  }
  .label {
    position: relative;
    width: 900px;
    height: 1200px;
    background: var(--label-ground);
    color: var(--label-cream);
    overflow: hidden;
  }
  .label-frame {
    position: absolute;
    inset: 0;
  }
  .brand {
    position: absolute;
    left: 0;
    right: 0;
    top: 372px;
    text-align: center;
    font-family: "Staatliches", sans-serif;
    line-height: 1;
  }
  .brand-name {
    font-size: 92px;
    letter-spacing: 2px;
  }
  .brand-sub {
    margin: 10px auto 0;
    width: 418px;
    padding: 6px 0 4px;
    border-top: 2px solid var(--label-cream);
    border-bottom: 2px solid var(--label-cream);
    font-size: 40px;
    letter-spacing: 9px;
    text-indent: 9px;
  }
  .product {
    position: absolute;
    left: 0;
    right: 0;
    top: 636px;
    text-align: center;
    font-family: "Staatliches", sans-serif;
    line-height: 1;
  }
  .product-name {
    font-size: 124px;
    letter-spacing: 1px;
  }
  .product-type {
    margin-top: 6px;
    font-size: 31px;
    letter-spacing: 3px;
  }
  .volume {
    position: absolute;
    left: 0;
    right: 0;
    top: 924px;
    text-align: center;
    font-family: "Staatliches", sans-serif;
    font-size: 50px;
    line-height: 1;
    letter-spacing: 1px;
  }
  .strength {
    position: absolute;
    top: 1040px;
    font-family: "Old Standard TT", serif;
    font-size: 25px;
    line-height: 1;
  }
  .strength-proof { left: 178px; }
  .strength-abv { right: 165px; }
</style>
</head>
<body>
<main class="label">
  <svg class="label-frame" width="900" height="1200" viewBox="0 0 900 1200" aria-hidden="true">
    <g fill="none" stroke="var(--label-cream)" stroke-width="3">
      <path d="M137 82 H763 A55 55 0 0 0 818 137 V1063 A55 55 0 0 0 763 1118 H137 A55 55 0 0 0 82 1063 V137 A55 55 0 0 0 137 82 Z"/>
      <path d="M140 108 H760 A32 32 0 0 0 792 140 V1060 A32 32 0 0 0 760 1092 H140 A32 32 0 0 0 108 1060 V140 A32 32 0 0 0 140 108 Z"/>
      <line x1="108" y1="195" x2="352" y2="195"/>
      <line x1="548" y1="195" x2="792" y2="195"/>
      <line x1="108" y1="295" x2="352" y2="295"/>
      <line x1="548" y1="295" x2="792" y2="295"/>
      <line x1="108" y1="883" x2="792" y2="883"/>
    </g>
    <circle class="brand-mark" cx="450" cy="240" r="92" fill="var(--label-cream)"/>
  </svg>

  <header class="brand">
    <div class="brand-name">Harrowgate</div>
    <div class="brand-sub">Distillery</div>
  </header>

  <section class="product">
    <h1 class="product-name" style="margin:0;font-weight:400;">Cedar Lorne</h1>
    <div class="product-type">Straight Bourbon Whiskey</div>
  </section>

  <div class="volume">750 ml</div>
  <div class="strength strength-proof">84 PROOF</div>
  <div class="strength strength-abv">42% ALC/VOL</div>
</main>
</body>
</html>
```